Packaging for coffee beans bag

looking for design for bags packaging for our coffee beans brand (logo attached) with special green color (you can select the best green color grade) for the sizes 1KG and 500GRAMS.
attached also pictures for our old packaging what we are looking to change.
attached the ai file for the final project.

```html
<!DOCTYPE html>
<html lang="en">
<head>
<meta charset="utf-8">
<title>Nakhla Roasters – Coffee Bag</title>
<link href="https://fonts.googleapis.com/css2?family=Reem+Kufi:wght@500&family=Montserrat:wght@500;600&family=Open+Sans:wght@400&display=swap" rel="stylesheet">
<style>
  :root {
    --stage: #e4e4e4;
    --bag-green: #6f8a56;
    --bag-charcoal: #33363d;
    --sticker-green: #a9d79b;
    --ink-light: #e9ece6;
    --ink-muted: #c9cfc3;
    --ink-dark: #2f3a2a;
  }
  html, body {
    margin: 0;
    width: 1200px;
    height: 880px;
    overflow: hidden;
    background: var(--stage);
  }
  .canvas { display: block; width: 1200px; height: 880px; }
  .brand-latin { font-family: 'Montserrat', sans-serif; font-weight: 600; fill: var(--ink-light); }
  .brand-arabic { font-family: 'Reem Kufi', sans-serif; font-weight: 500; fill: var(--ink-light); }
  .opening-note { font-family: 'Montserrat', sans-serif; font-weight: 500; fill: var(--ink-muted); }
  .sticker-label { font-family: 'Open Sans', sans-serif; font-weight: 400; fill: var(--ink-dark); }
</style>
</head>
<body>
<svg class="canvas" viewBox="0 0 1200 880" xmlns="http://www.w3.org/2000/svg">
  <defs>
    <pattern id="wave-edge" x="0" y="0" width="10" height="12" patternUnits="userSpaceOnUse">
      <path d="M10 0 L2 6 L10 12 Z" fill="var(--bag-charcoal)"/>
    </pattern>
    <clipPath id="bag-clip">
      <rect x="330" y="40" width="540" height="800"/>
    </clipPath>
  </defs>

  <g class="bag-front" clip-path="url(#bag-clip)">
    <rect class="bag-body" x="330" y="40" width="540" height="800" fill="var(--bag-green)"/>
    <rect class="bag-band" x="660" y="40" width="210" height="800" fill="var(--bag-charcoal)"/>
    <rect class="bag-band-edge" x="650" y="40" width="10" height="800" fill="url(#wave-edge)"/>
    <rect class="top-seal" x="330" y="40" width="540" height="14" fill="#000" opacity="0.12"/>

    <g class="opening-guide">
      <rect x="362" y="132" width="22" height="22" rx="4" fill="none" stroke="var(--ink-muted)" stroke-width="1.5"/>
      <text class="opening-note" x="373" y="147" font-size="8" text-anchor="middle">TAB</text>
      <text class="opening-note" x="394" y="147" font-size="10">PULL TAB TO OPEN</text>
      <g fill="var(--ink-muted)">
        <path d="M510 138 l8 4 l-8 4 z"/><path d="M532 138 l8 4 l-8 4 z"/>
        <path d="M554 138 l8 4 l-8 4 z"/><path d="M576 138 l8 4 l-8 4 z"/>
        <path d="M598 138 l8 4 l-8 4 z"/><path d="M620 138 l8 4 l-8 4 z"/>
        <path d="M642 138 l8 4 l-8 4 z"/><path d="M664 138 l8 4 l-8 4 z"/>
        <path d="M686 138 l8 4 l-8 4 z"/><path d="M708 138 l8 4 l-8 4 z"/>
        <path d="M730 138 l8 4 l-8 4 z"/><path d="M752 138 l8 4 l-8 4 z"/>
      </g>
      <line class="zipper-line" x1="362" y1="176" x2="840" y2="176" stroke="var(--ink-muted)" stroke-width="4" stroke-dasharray="4 4"/>
      <rect x="580" y="164" width="62" height="14" fill="var(--bag-charcoal)"/>
      <text class="opening-note" x="611" y="175" font-size="10" text-anchor="middle">ZIPPER</text>
    </g>

    <g class="brand-small">
      <circle cx="440" cy="262" r="9" fill="var(--ink-light)"/>
      <text class="brand-latin" x="440" y="298" font-size="22" text-anchor="middle" letter-spacing="1">NAKHLA</text>
      <text class="brand-latin" x="440" y="314" font-size="9" text-anchor="middle" letter-spacing="4">ROASTERS</text>
    </g>

    <circle class="brand-dot" cx="765" cy="250" r="28" fill="var(--ink-light)"/>
    <text class="brand-arabic" x="765" y="550" font-size="100" text-anchor="middle" dominant-baseline="central" textLength="480" lengthAdjust="spacingAndGlyphs" transform="rotate(-90 765 550)">محمصة النخلة</text>

    <rect class="sticker-area" x="360" y="560" width="280" height="250" rx="22" fill="var(--sticker-green)" stroke="var(--ink-light)" stroke-width="2"/>
    <text class="sticker-label" x="386" y="786" font-size="17">place for sticker</text>
  </g>
</svg>
</body>
</html>
```